Walk Bold Stay Kind Ebook and Print book cover

I need a professional, eye catching cover that will stand out. The title of the book is "Walk Bold Stay Kind: 47 Quiet Rules For Calm and Wonder" It is a self-help personal transformation book by author Dale Ormsby. The cover will be on both print and ebook covers. I want something that is similar yet different to best-selling books in the genre, nothing too boring. A blue background might work, but it isn't a requirement. I'm open to other colors as long as it's powerful, professional, and screams "Buy me because this book is going to change your life!"
Updates

So far, 3 designs (3 of the 4 star rated designs) are in contention, but they all can be improved. I think the book cover should best convey "thinking smart" in a dynamic way. I'll run another poll in a day or so when I get additional designs I like. Added Thursday, May 4, 2017

Based on current designs, I wanted to provide additional guidance. The title and image should pop and be clearly visible at a distance as a thumbnail. Also, I'm wanting something bold and creative but not too confusing. I currently have a couple solid designs that are in contention to win, but I have another 7 days left for the project. I extended it to 10 days from the initial 5. I'll include several more polls for my followers and will likely pick the top ranking design based off the series of polls and will be eliminating lower ranking designs with each new poll and set of promising designs that come in. Finally, I may ask to see what the back will look like on the print version since I'll need both the Lumora and print (5" by 8") designs. Added Saturday, May 6, 2017

It's been recommended by some that I should have my own picture on the cover. I'm not completely convinced, but I would like to see some additional designs that incorporate my photo (touched up to remove the shine from my forehead and the label brand name removed from the t-shire) into a cover design. I have several good designs coming in, so typeset and professional looking font is extremely important. Blue is also preferred but not required. I've attached the photo on the brief for those who want to submit a design with that photo. Added Saturday, May 6, 2017

Target Market(s)

Working age adults seeking personal transformation and self improvement.

Industry/Entity Type

Motivation

Requirements
Must have
• Creativity. Eye catching. Striking. Contrast. Looks good close up and as a thumbnail at a distance. Font should be easy to read and pop from the cover along with the design.
Nice to have
• Powerful image placement. Play up the "Walk Bold" aspect of the title. Perhaps even contrasting someone who's thinking "Hard." Here are a few examples of intriguing covers (though not necessarily related to the genre) I like mainly for aesthetics and creativity. https://www.shopvale.com/dp/Q71MRT2KWD/ https://www.shopvale.com/dp/Q34PLN8XEA
• https://www.shopvale.com/dp/Q925GHV3TC/
• https://www.shopvale.com/dp/Q48DJW6RZB/
• (the font is a little poor in the last one but the image is evoking)
Should not have
• Ugly, tacky, or hard to read fonts. A simple photo with text on top. A simple background with words. Confusing images. Designs with no additional stock image purchase requirements will be given preference over those that do. I've seen a lot of balloons and light bulbs. I'm not saying you can't include them in the design, but if you want to stand out, try to find something more creative that expresses the concept of the title.

```html
<!DOCTYPE html>
<html lang="en">
<head>
<meta charset="utf-8">
<title>Walk Bold Stay Kind — Full Wrap Cover</title>
<link rel="stylesheet" href="https://fonts.googleapis.com/css2?family=Oswald:wght@600;700&family=Cormorant+Garamond:ital,wght@0,500;1,500&display=swap">
<style>
  :root {
    --blue-deep: #0a1f7a;
    --blue-bright: #0b3bd0;
    --navy: #0b1a55;
    --orange: #ff8a00;
    --orange-dark: #e06e00;
    --yellow: #f3b800;
    --white: #ffffff;
  }
  * { margin: 0; padding: 0; box-sizing: border-box; }
  html, body { width: 1200px; height: 914px; overflow: hidden; background: #fff; }
  .cover { position: relative; width: 1200px; height: 914px; overflow: hidden; }

  /* Back cover */
  .back { position: absolute; left: 0; top: 0; width: 572px; height: 914px;
    background: radial-gradient(ellipse at 50% 20%, var(--blue-bright), var(--blue-deep) 90%); }
  .back-lower { position: absolute; left: 0; top: 464px; width: 572px; height: 450px;
    background: linear-gradient(180deg, var(--orange) 70%, var(--orange-dark)); }
  .back-title { position: absolute; left: 166px; top: 48px; color: var(--white);
    font-family: "Oswald", sans-serif; font-weight: 700; line-height: .86; white-space: nowrap;
    transform: rotate(-3deg) skewY(-2deg); transform-origin: left top; }
  .back-title .line-small { display: block; font-size: 46px; }
  .back-title .line-big { display: block; font-size: 78px; }
  .blurb { position: absolute; left: 28px; width: 508px; color: var(--white);
    font-family: "Cormorant Garamond", serif; font-weight: 500; font-size: 17.4px;
    line-height: 22.9px; text-align: justify; hyphens: auto; }
  .blurb-one { top: 226px; }
  .blurb-two { top: 477px; }
  .code-box { position: absolute; left: 40px; top: 756px; width: 158px; height: 122px; background: var(--white); }

  /* Spine */
  .spine { position: absolute; left: 572px; top: 0; width: 57px; height: 914px; background: var(--navy); }
  .spine-title, .spine-author { position: absolute; left: 50%; color: var(--white);
    white-space: nowrap; transform: translate(-50%, -50%) rotate(-90deg); }
  .spine-title { top: 190px; font-family: "Oswald", sans-serif; font-weight: 700; font-size: 35px; letter-spacing: -.5px; }
  .spine-author { top: 586px; font-family: "Cormorant Garamond", serif; font-weight: 500; font-size: 38px; }
  .spine-photo { position: absolute; left: 4px; top: 840px; width: 49px; height: 74px;
    background: linear-gradient(180deg, #b98a6a, #1c2b5e 60%); }

  /* Front cover */
  .front { position: absolute; left: 629px; top: 0; width: 571px; height: 914px; background: var(--navy); }
  .front-bands { position: absolute; inset: 0; }
  .portrait { position: absolute; left: 35px; top: 256px; width: 368px; height: 556px;
    background: linear-gradient(180deg, #8a6550 0%, #6d5040 28%, #1b2c63 48%, #14214f 100%);
    border-radius: 160px 160px 0 0; }
  .front-title { position: absolute; left: 50px; top: 20px; width: 480px; color: var(--white);
    font-family: "Oswald", sans-serif; font-weight: 700; white-space: nowrap;
    transform: skewY(-5deg); transform-origin: left top; }
  .front-title .line-small { display: block; height: 63px; font-size: 92px; line-height: 1; }
  .front-title .line-big { display: block; height: 150px; font-size: 96px; line-height: 1; }
  .front-title .line-big span { display: inline-block; transform: scaleY(1.7); transform-origin: left top; }
  .subtitle { position: absolute; left: 244px; top: 268px; width: 330px; color: var(--white);
    font-family: "Cormorant Garamond", serif; font-style: italic; font-weight: 500;
    font-size: 42px; line-height: 1.05; text-align: center; transform: rotate(-8deg); }
  .author-band { position: absolute; left: 0; top: 812px; width: 571px; height: 102px;
    background: linear-gradient(90deg, var(--orange-dark), var(--orange) 40%, var(--orange-dark)); }
  .author-name { position: absolute; left: 0; top: 812px; width: 571px; height: 102px;
    display: flex; align-items: center; justify-content: center; color: var(--white); white-space: nowrap;
    font-family: "Cormorant Garamond", serif; font-weight: 500; font-size: 74px; letter-spacing: 2px; }
</style>
</head>
<body>
<main class="cover">
  <section class="back">
    <div class="back-lower"></div>
    <h2 class="back-title"><span class="line-small">WALK BOLD</span><span class="line-big">STAY KIND</span></h2>
    <p class="blurb blurb-one">Lorem ipsum dolor sit amet, consectetur adipiscing elit. Curabitur semper libero eget lectus tincidunt tristique. Fusce mollis augue urna, vitae pulvinar mi facilisis bibendum. Donec nec ullamcorper massa. Praesent sem neque, molestie ut nunc at, laoreet congue sem. Duis fringilla velit malesuada laoreet tincidunt. Aliquam eu luctus nulla. Phasellus suscipit, neque eu semper gravida, risus nisi consectetur lacus, a pretium orci diam quis nibh. Cras in accumsan erat. Ut id purus mi. Praesent lacinia felis nulla, ac venenatis leo luctus vitae. Etiam a fermentum nisl. Pellentesque sed varius sem.</p>
    <p class="blurb blurb-two">Maecenas tempor dolor lectus, a facilisis est placerat nec. Fusce eu mi id nulla commodo fermentum. Quisque luctus euismod mattis. Integer ultrices non purus sed semper. Vivamus dapibus efficitur est vitae ultrices. Phasellus nec dictum nisl, quis tristique purus. Aenean tristique tellus vel sagittis venenatis. Sed ipsum nisi, sollicitudin et varius sit amet, congue ut tellus. Mauris eu nunc et neque venenatis scelerisque. Pellentesque sed sapien sit amet justo sagittis sagittis. Cras quis nisl risus. Phasellus ac semper ligula, vestibulum pellentesque lorem. Curabitur sagittis</p>
    <div class="code-box"></div>
  </section>

  <section class="spine">
    <div class="spine-title">WALK BOLD STAY KIND</div>
    <div class="spine-author">DALE ORMSBY</div>
    <div class="spine-photo" role="img" aria-label="Small author portrait, thoughtful pose"></div>
  </section>

  <section class="front">
    <svg class="front-bands" width="571" height="914" viewBox="0 0 571 914" aria-hidden="true">
      <defs>
        <linearGradient id="yellowBand" x1="0" y1="0" x2="1" y2="1">
          <stop offset="0" stop-color="#f7c200"/><stop offset="1" stop-color="#d9a300"/>
        </linearGradient>
        <radialGradient id="blueField" cx="0.4" cy="0.5" r="0.8">
          <stop offset="0" stop-color="#0b34c0"/><stop offset="1" stop-color="#0a1b62"/>
        </radialGradient>
      </defs>
      <rect width="571" height="914" fill="url(#blueField)"/>
      <polygon points="0,0 571,0 571,180 0,68" fill="url(#yellowBand)"/>
      <polygon points="0,68 571,180 571,228 0,284" fill="#ff8a00"/>
    </svg>
    <div class="portrait" role="img" aria-label="Author portrait: man in a navy blazer, hand on chin, looking up in thought"></div>
    <h1 class="front-title"><span class="line-small">WALK BOLD</span><span class="line-big"><span>STAY KIND</span></span></h1>
    <p class="subtitle">47 Quiet Rules<br>For Calm<br>and Wonder</p>
    <div class="author-band"></div>
    <div class="author-name">DALE ORMSBY</div>
  </section>
</main>
</body>
</html>
```